Graphic lion print design with text

I like the gold effects in image 2 as described in my attached document, but i'm open to other suggestions. The desired image is image 1. This is a gift for a Leo friend. This is going to be printed and framed to be hung on the wall in a large frame, in landscape format. I like the idea of using different font styles to separate the statements.

Requirements
Must have
• I’m open to the suggestions about the font styles, but I want to separate the statements by using different font styles as shown in attached document.
Must be landscape format.
Small fonts preferred, as shown in the attached image.
Nice to have
• I like the gold effect in image 2 but other suggestions/colours welcome
Should not have
• Please don't stretch the picture so I can have a good resolution. Place the text on another black background template and then paste the picture beside to the text.

```html
<!DOCTYPE html>
<html lang="en">
<head>
<meta charset="utf-8">
<title>Lion Blessing Print</title>
<link rel="stylesheet" href="https://fonts.googleapis.com/css2?family=Courgette&family=Cinzel:wght@500&family=Lora&family=Marcellus&family=Montserrat:wght@700&family=Comfortaa:wght@400&display=swap">
<style>
  :root {
    --ink: #000000;
    --gold: #f2b705;
    --gold-text: #e8b10c;
    --gold-deep: #8a5a08;
    --gold-mid: #c98a12;
  }
  html, body {
    margin: 0;
    padding: 0;
    width: 1200px;
    height: 801px;
    overflow: hidden;
    background: var(--ink);
  }
  .print {
    position: relative;
    width: 1200px;
    height: 801px;
    background: var(--ink);
    color: var(--gold-text);
  }
  .print__border {
    position: absolute;
    left: 11px;
    top: 11px;
    width: 1162px;
    height: 764px;
    border: 7px solid var(--gold);
  }
  .line {
    position: absolute;
    margin: 0;
    white-space: nowrap;
    transform: translate(-50%, -50%);
    text-align: center;
    line-height: 1;
  }
  .script { font-family: "Courgette", cursive; font-weight: 400; }
  .caps-serif { font-family: "Cinzel", serif; font-weight: 500; }
  .book-serif { font-family: "Lora", serif; }
  .classic { font-family: "Marcellus", serif; }
  .bold-sans { font-family: "Montserrat", sans-serif; font-weight: 700; }
  .rounded { font-family: "Comfortaa", sans-serif; }

  .headline { left: 620px; top: 54px; font-size: 27px; }
  .promise-box {
    position: absolute;
    left: 443px;
    top: 83px;
    width: 365px;
    height: 42px;
    border: 2px solid var(--gold);
    box-sizing: border-box;
    display: flex;
    align-items: center;
    justify-content: center;
    font-size: 25px;
  }
  .conqueror { left: 630px; top: 148px; font-size: 22px; }

  .rule {
    position: absolute;
    height: 2px;
    background: linear-gradient(90deg, transparent, var(--gold) 15%, var(--gold) 85%, transparent);
  }
  .rule--top { left: 374px; top: 171px; width: 514px; }
  .rule--one { left: 131px; top: 366px; width: 532px; }
  .rule--two { left: 131px; top: 522px; width: 532px; }

  .almighty { left: 400px; top: 211px; font-size: 28px; }
  .come-through { left: 399px; top: 256px; font-size: 26px; letter-spacing: 0.5px; }
  .seek { left: 399px; top: 300px; font-size: 29px; }
  .moments { left: 399px; top: 340px; font-size: 23px; letter-spacing: 0.5px; }

  .may-god { left: 399px; top: 398px; font-size: 24px; }
  .calm { left: 399px; top: 430px; font-size: 24px; letter-spacing: 1px; }
  .ampersand { left: 399px; top: 462px; font-size: 22px; }
  .still { left: 399px; top: 495px; font-size: 24px; letter-spacing: 0.5px; }

  .doors { left: 399px; top: 548px; font-size: 25px; letter-spacing: 1px; }
  .open { left: 399px; top: 582px; font-size: 25px; letter-spacing: 0.5px; }
  .unlikeliest { left: 399px; top: 614px; font-size: 22px; letter-spacing: 0.5px; }

  .closing-box {
    position: absolute;
    left: 205px;
    top: 648px;
    width: 843px;
    height: 115px;
    border: 2px solid var(--gold);
    box-sizing: border-box;
    display: flex;
    flex-direction: column;
    align-items: center;
    justify-content: center;
    font-size: 24px;
    line-height: 36px;
    text-align: center;
  }

  .lion-art {
    position: absolute;
    left: 807px;
    top: 119px;
    width: 370px;
    height: 568px;
    background:
      radial-gradient(ellipse 55% 50% at 70% 50%, var(--gold-mid) 0%, var(--gold-deep) 55%, rgba(0,0,0,0) 100%);
  }
</style>
</head>
<body>
  <main class="print">
    <div class="print__border"></div>

    <p class="line script headline">It doesn't matter who or what may come against you</p>
    <div class="promise-box caps-serif">FOR GOD IS WITH YOU</div>
    <p class="line book-serif conqueror">HE has made you more than a conqueror.</p>
    <div class="rule rule--top"></div>

    <p class="line script almighty">Almighty GOD</p>
    <p class="line bold-sans come-through">will come through for you</p>
    <p class="line script seek">when you Seek Him</p>
    <p class="line bold-sans moments">in your moments of trouble &amp; unrest</p>
    <div class="rule rule--one"></div>

    <p class="line classic may-god">MAY GOD</p>
    <p class="line classic calm">calm the restlessness of your mind</p>
    <p class="line bold-sans ampersand">&amp;</p>
    <p class="line bold-sans still">still the thouhgts that worry you.</p>
    <div class="rule rule--two"></div>

    <p class="line bold-sans doors">DOORS</p>
    <p class="line book-serif open">will open for you,</p>
    <p class="line bold-sans unlikeliest">in the most unlikeliest of places.</p>

    <div class="lion-art" role="img" aria-label="Gold glitter illustration of a roaring lion's head in profile"></div>

    <div class="closing-box rounded">
      <span>When you go through deep waters. He will be with you.</span>
      <span>Never will He leave you. Never will He forsake you.</span>
      <span>Amen.</span>
    </div>
  </main>
</body>
</html>
```